Brochure Design Project - Innovative Service for Pharma Industry

Our start up is based in Germany, near Munich and we provide an innovative Service for the pharma industry. We develop product trainings and general trainings online. The adressed audience for these trainings are pharmacies and medics. The parma industry could increase the number of trainings, while saving money (incl a success guarantee). Our (not yet finnished) corporate page can be reviewed here: www.brevoloq.biz, our 'product & service' page is www.kestrumlearn.com. The color code should be leaned towards the corporate page.

The brochure should be send to decision makers in the pharma industry and rise the interest in innovative service. Seriousity should meet modern & clear design.Something eye cathing on the front page might be required.

Target Market(s)

Usually more conservative decision makers within the pharma industry

Industry/Entity Type

Industry

Requirements
Must have
• Conceptional design for an brochure (Din A4 size) of approx 6-8 pages, that capture the key messages (exact content would be filled / provided from us)
Nice to have
• Implementing some of the pics / phrases on the home page www.brevolq.biz could be maybe nice. How about a personal statement from the founder combined with a pic(pic attached)? Both is no must....

```html
<!DOCTYPE html>
<html lang="de">
<head>
<meta charset="utf-8">
<title>Brevoloq – Broschüre</title>
<link href="https://fonts.googleapis.com/css2?family=Dosis:wght@400;500;600&display=swap" rel="stylesheet">
<style>
:root{
  --orange:#d4502f;
  --text:#2a2a2a;
  --band:#5b5b5b;
  --canvas:#e4e5e6;
  --page:#ffffff;
  --logo-grey:#8c8c8c;
  --partner:#2b4a8a;
}
*{margin:0;padding:0;box-sizing:border-box}
html,body{width:1200px;height:3311px;overflow:hidden;background:var(--canvas)}
body{position:relative;font-family:"Dosis",sans-serif;color:var(--text)}
.page{position:absolute;left:38px;width:1124px;background:var(--page);overflow:hidden}
.page--service{top:34px;height:1593px}
.page--benefits{top:1682px;height:1591px}
.header-tab{position:absolute;left:560px;top:0;width:564px;height:118px;background:var(--orange);color:#fff;
  font-size:44px;font-weight:500;display:flex;align-items:center;justify-content:center;letter-spacing:.5px}
.col{position:absolute;font-size:19px;line-height:20.5px;text-align:justify}
.col h2{color:var(--orange);font-weight:400;font-size:30px;line-height:34px;margin-bottom:18px}
.col h3{color:var(--orange);font-weight:400;font-size:19px;line-height:20.5px}
.col p{margin-bottom:20.5px}
.col h2.later{margin-top:26px}
.photo{position:absolute}
.band{position:absolute;left:0;width:1124px;background:var(--band)}
.logo-box{position:absolute;left:125px;width:193px;height:150px;background:#fff;box-shadow:0 2px 8px rgba(0,0,0,.35);
  display:flex;flex-direction:column;align-items:center;justify-content:flex-end;padding-bottom:14px}
.logo-box .dot{width:66px;height:66px;border-radius:50%;background:#b9b9b9;margin-bottom:10px}
.logo-box .name{font-size:34px;font-weight:600;color:var(--orange);line-height:34px}
.logo-box .tag{font-size:9px;color:var(--logo-grey);letter-spacing:1px;margin-top:3px}
.partner-name{position:absolute;font-size:26px;font-weight:600;color:var(--partner)}
.intro{position:absolute;left:637px;top:164px;width:423px;font-size:19px;line-height:21px;color:var(--orange);text-align:justify}
.intro p{margin-bottom:21px}
</style>
</head>
<body>

<section class="page page--service">
  <div class="header-tab">unser service</div>

  <div class="col" style="left:71px;top:243px;width:427px">
    <h2>Academy</h2>
    <p>Willkommen bei der größten unabhängigen Pharma E-Learning Plattform Deutschlands. Unsere Online Academy bildet das Herzstück unseres umfassenden Services für Apotheken, Praxen und Kliniken.</p>
    <p>Sie werden im Laufe der Zeit eine stetig steigende Anzahl von Schulungen rund um den pharmazeutischen und medizinischen Bereich finden. Die Produktschulungen sind von den jeweiligen Herstellern zertifiziert und adressieren ausschließlich medizinisches Fachpersonal.</p>
    <p>Um Zugang zu der Academy zu bekommen und um von den zahlreichen Vorteilen profitieren zu können, erfordert es eine einmalige Registrierung von Ihnen und eine Verifizierung von uns.</p>
    <p>Der Vorgang geht schnell und Sie können nach einer kurzen Verifikation bereits auf – für Sie zugängliche – Kurse zugreifen.</p>
    <h2 class="later">Bonusshop</h2>
    <p>Bei vielen unserer Produktschulungen und Tests können Sie Bonuspunkte sammeln.</p>
    <p>Wenn Sie genügend Bonuspunkte gesammelt haben, können Sie diese in wertvolle und attraktive Prämien eintauschen. Der Auswahl der Prämien ist umfangreich und wird ständig aktualisiert. Wir sind sicher, für jeden Geschmack etwas anbieten zu können.</p>
    <p>Viel Spaß mit Ihrer Prämie</p>
    <h2 class="later">Informationen</h2>
    <p>Unsere Online Service Plattform soll für unsere Nutzer zentral, einfach, vorteilhaft &amp; die Schulungen kostenlos sein.</p>
    <p>Um Ihnen Ihre Fragen weitestgehend zu beantworten, haben wir Informationen zu den verschiedensten Themengebieten zur Verfügung gestellt. Falls Sie weitere Informationen benötigen, können Sie uns über das Kontaktformular erreichen oder einfach unsere Infoline anrufen. Sie erreichen uns dort von Montag bis Freitags von 09.00 -18.00 Uhr.</p>
  </div>

  <div class="col" style="left:637px;top:243px;width:423px">
    <h2>Partner</h2>
  </div>
  <div class="partner-name" style="left:637px;top:300px">Veltamed</div>
  <div class="partner-name" style="left:841px;top:300px">Orsanta</div>

  <div class="photo" role="img" aria-label="Foto: Ärztin im weißen Kittel arbeitet entspannt am Laptop"
       style="left:560px;top:734px;width:564px;height:743px;background:linear-gradient(160deg,#f4f6f6 0%,#dfe4e3 55%,#c9d0cf 100%)"></div>

  <div class="band" style="top:1477px;height:116px"></div>
  <div class="logo-box" style="top:1421px">
    <div class="dot"></div>
    <div class="name">brevoloq</div>
    <div class="tag">THE E-LEARNING COMPANY</div>
  </div>
</section>

<section class="page page--benefits">
  <div class="header-tab">vorteile</div>

  <div class="intro">
    <p>Als unabhängiger Dienstleister bietet Kestrumlearn eine Vielzahl verschiedener Vorteile für unterschiedliche Berufsgruppen aus dem pharmazeutischen Umfeld.</p>
    <p>Mit Hilfe des nebenstehenden Menüs können Sie sich im Detail über Ihren individuellen Nutzen informieren.</p>
  </div>

  <div class="col" style="left:86px;top:400px;width:464px">
    <h2 style="margin-bottom:10px">Apothekenmitarbeiter</h2>
    <h3>Großes Schulungsangebot</h3>
    <p>Kestrumlearn bietet Ihnen eine zentrale Anlaufstelle für zukünftige Produktschulungen der Pharmaindustrie. Unsere Online Academy dient als Service Plattform und verfügt über eine große Auswahl von Schulungen verschiedenster Pharmaunternehmen. Die Inhalte sind so zusammengestellt, dass Sie mit minimalem Zeitaufwand ein Maximum an Wissen vermittelt bekommen.</p>
    <p>Verschwenden Sie keine Zeit mehr und bleiben Sie mehr denn je immer auf dem neusten Stand!</p>
    <h3>Flexibilität</h3>
    <p>Sie entscheiden selber, welche Trainings und Schulungen Sie belegen möchten.</p>
    <p>Zusätzlich haben Sie völlige Freiheit, selbst zu entscheiden wann und wo Sie dies machen möchten, zum Beispiel daheim auf Ihrem Sofa. Keine stundenlangen Sitzungen mehr nach Feierabend in der Apotheke. Die Trainings sind so konzipiert, dass Sie in der Regel nicht länger als ca. 15 Minuten dafür benötigen.</p>
    <h3>Zertifikat</h3>
    <p>Schulungen jeder Art sind ein Teil Ihrer persönlichen Weiterbildung. Ihr Wissen bestimmt Ihren Wert gegenüber Ihrem Arbeitgeber. Für Sie und natürlich auch für Ihren Arbeitgeber empfiehlt es sich daher Ihre Qualitäten zu belegen, indem Sie Zertifikate für die erfolgreich abgeschlosseneren Trainings bekommen. Dies erfolgt bei Kestrumlearn automatisch und sofort – so geht Ihnen nichts verloren.</p>
    <p>Diese Zertifikate erleichtern Ihrem Arbeitgeber auch die Qualitätssicherung innerhalb seiner Apotheke</p>
    <h3>Bonussystem</h3>
    <p>Sich weiterbilden und dafür auch noch etwas bekommen?</p>
  </div>

  <div class="col" style="left:637px;top:405px;width:423px">
    <p>erfolgreich abschließen bekommen Sie Bonuspunkte. Die gesammelten Bonuspunkte können Sie anschließend in unserem Bonusshop in wertvolle Prämien einlösen.</p>
    <p>Zusätzlich führen wir immer wieder Verlosungen von interessanten Preisen unter allen Neuanmeldungen &amp; Teilnehmern durch.</p>
    <p>Mitmachen lohnt sich also mehrfach für Sie.</p>
  </div>

  <div class="photo" role="img" aria-label="Foto: lächelnde Apothekerin am Verkaufstresen vor Regalen einer Apotheke"
       style="left:560px;top:1100px;width:564px;height:375px;background:linear-gradient(100deg,#c7cfd0 0%,#e9e3d6 45%,#f1ece4 70%,#c9a98a 100%)"></div>

  <div class="band" style="top:1475px;height:116px"></div>
  <div class="logo-box" style="top:1423px">
    <div class="dot"></div>
    <div class="name">brevoloq</div>
    <div class="tag">THE E-LEARNING COMPANY</div>
  </div>
</section>

</body>
</html>
```